exciting cleaing project

I need a cleaning website built. It has to be built for a woman. the domain name is gwenshines.net.

I need the designer to find the images and code the site. the site needs to be about five pages.

here are some good examples:

https://www.tidypetal.com/gainesville/

http://abrightwren.com/

https://brisknookgainesville.com/services/

https://www.hevo.com/housekeepers/gainesville-fl

https://glintrow.com/

Target Market(s)

home cleaning,

Industry/Entity Type

Cleaning Service

Coding

Coded - Design and coding required

Number of Pages Required

4 page

Font styles to use
Script

Colors
33a6d7
85acd3
f04a50
ec1f27

Requirements
Must have
• nice design
Nice to have
• residential
Should not have
• commercial

```html
<!DOCTYPE html>
<html lang="en">
<head>
<meta charset="utf-8">
<title>Gwen Shines – Home Cleaning</title>
<link rel="stylesheet" href="https://fonts.googleapis.com/css2?family=Open+Sans:wght@400;600;700&family=Lato:wght@400;700&display=swap">
<style>
:root{
  --red:#f04a50;
  --red-deep:#ec1f27;
  --blue:#33a6d7;
  --blue-soft:#85acd3;
  --footer-blue:#3189b1;
  --ink:#222;
  --muted:#6b6b6b;
  --white:#fff;
  --black:#0d0d0d;
}
*{box-sizing:border-box;margin:0;padding:0}
html,body{width:1200px;height:3212px;overflow:hidden}
body{position:relative;font-family:"Lato",sans-serif;color:var(--ink);background:var(--white)}
.section{position:absolute;left:0;width:1200px}
.head-font{font-family:"Open Sans",sans-serif}

/* top bar */
.top-bar{top:0;height:51px;background:var(--red);color:var(--white);font-size:13px}
.top-bar .contact{position:absolute;left:100px;top:0;height:51px;display:flex;align-items:center;gap:12px}
.top-bar .contact span{display:flex;align-items:center;gap:8px}
.top-bar .divider{width:1px;height:26px;background:rgba(255,255,255,.6)}
.top-bar .estimate{position:absolute;right:99px;top:9px;height:32px;padding:0 12px;border:1px solid var(--white);display:flex;align-items:center;font-size:12px;letter-spacing:.2px}

/* header */
.site-header{top:51px;height:109px;background:var(--white)}
.brand{position:absolute;left:100px;top:30px;display:flex;align-items:center;gap:10px;font-family:"Open Sans",sans-serif;font-weight:700;font-size:20px;color:var(--red)}
.brand .mark{width:40px;height:40px;border-radius:50%;background:var(--red)}
.main-nav{position:absolute;right:99px;top:44px;display:flex;gap:34px;font-size:13px;font-weight:600;font-family:"Open Sans",sans-serif}
.main-nav a{color:var(--ink);text-decoration:none;padding-bottom:6px}
.main-nav a.active{border-bottom:2px solid var(--red)}

/* hero */
.hero{top:160px;height:580px}
.hero-photo{position:absolute;inset:0;background:linear-gradient(90deg,#d9dadc 0%,#c9cacc 45%,#b8b1ad 65%,#c24a40 80%,#d8d5d2 100%)}
.hero-box{position:absolute;left:99px;top:114px;width:380px;height:300px;background:rgba(133,172,211,.85);color:var(--white);padding:20px 18px}
.hero-box h1{font-family:"Open Sans",sans-serif;font-weight:400;font-size:30px;letter-spacing:.3px}
.hero-box p{font-size:14px;line-height:17px;margin-top:10px;width:330px}
.hero-list{display:grid;grid-template-columns:192px 150px;row-gap:14px;margin-top:18px;font-family:"Open Sans",sans-serif;font-size:15px}
.hero-list li{list-style:none;display:flex;align-items:center;gap:10px}
.btn-outline{display:inline-flex;align-items:center;border:2px solid currentColor;font-family:"Open Sans",sans-serif;font-weight:700;font-size:13px;padding:0 12px;height:32px}
.hero-box .btn-outline{margin-top:22px;color:var(--white)}

/* provide */
.provide{top:740px;height:461px;background:linear-gradient(180deg,#f4f5f6 0%,#e9ebec 55%,#dfe2e4 100%)}
.provide-text{position:absolute;left:99px;top:115px;width:540px}
.provide-text h2{font-family:"Open Sans",sans-serif;font-weight:600;color:var(--red);font-size:29px}
.provide-text h3{font-family:"Open Sans",sans-serif;font-weight:400;color:var(--blue);font-size:16px;margin-top:6px;letter-spacing:.2px}
.provide-text p{font-size:14px;line-height:22px;margin-top:12px;width:490px}
.provide-text .btn-outline{margin-top:16px;color:var(--ink);height:32px;padding:0 16px}
.provide-photo{position:absolute;left:673px;top:89px;width:427px;height:275px;border:4px solid var(--white);background:linear-gradient(135deg,#dcb37f 0%,#e3c08f 40%,#d6453e 60%,#c8b7a2 100%)}

/* services */
.services{top:1201px;height:657px;background:linear-gradient(90deg,#3b3735 0%,#5b5755 45%,#4a4441 100%);color:var(--white);text-align:center}
.services h2{position:absolute;top:52px;width:100%;font-family:"Open Sans",sans-serif;font-weight:600;font-size:28px}
.services .sub{position:absolute;top:94px;width:100%;font-family:"Open Sans",sans-serif;font-size:16px}
.services .lead{position:absolute;top:126px;left:250px;width:700px;font-size:14px;line-height:22px}
.service-card{position:absolute;top:218px;width:282px;height:293px;background:var(--white)}
.service-card .ring{position:absolute;left:52px;top:40px;width:178px;height:178px;border:3px solid var(--blue);border-radius:50%;display:flex;align-items:center;justify-content:center}
.service-card h4{position:absolute;top:236px;width:100%;font-family:"Open Sans",sans-serif;font-weight:600;font-size:20px;color:var(--red)}
.services .btn-outline{position:absolute;top:549px;left:521px;width:156px;justify-content:center;color:var(--white)}

/* hours */
.hours{top:1858px;height:449px;background:linear-gradient(180deg,#ececec 0%,#dcdcdc 50%,#e9e9e9 100%)}
.hours-card{position:absolute;left:100px;top:96px;width:383px;height:253px;background:rgba(255,255,255,.75);padding:8px}
.hours-card .inner{border:3px solid var(--blue);height:100%;text-align:center;padding-top:28px}
.hours-card h2{font-family:"Open Sans",sans-serif;font-weight:600;color:var(--red);font-size:27px}
.hours-card .note{font-family:"Open Sans",sans-serif;color:var(--blue);font-size:15px;margin-top:4px}
.hours-card .label{font-family:"Open Sans",sans-serif;font-size:16px;margin-top:18px}
.hours-card .time{font-family:"Open Sans",sans-serif;font-size:16px;margin-top:12px}
.contact-tile{position:absolute;left:675px;width:425px;background:rgba(255,255,255,.75);padding:8px}
.contact-tile .inner{border:3px solid var(--blue);height:100%;display:flex;align-items:center;justify-content:center;gap:18px;font-family:"Open Sans",sans-serif;font-weight:600;font-size:28px;color:#333}

/* news */
.news{top:2307px;height:540px}
.news h2{position:absolute;top:40px;width:100%;text-align:center;font-family:"Open Sans",sans-serif;font-weight:600;font-size:28px;color:var(--red)}
.post{position:absolute;top:98px;width:278px}
.post .thumb{height:197px}
.post h3{font-family:"Open Sans",sans-serif;font-weight:400;font-size:17px;color:#444;margin-top:16px}
.post p{font-size:12px;line-height:20px;color:var(--muted);margin-top:10px}
.post .more{border-top:1px solid #bbb;border-bottom:1px solid #bbb;margin-top:14px;height:46px;display:flex;align-items:center;padding-left:4px;font-size:12px;color:var(--red);gap:5px}

/* footer */
.site-footer{top:2847px;height:305px;background:var(--footer-blue);color:var(--white)}
.site-footer h5{font-family:"Open Sans",sans-serif;font-weight:600;font-size:15px}
.foot-col{position:absolute;top:57px}
.foot-contact div{display:flex;align-items:center;gap:10px;font-size:12px;margin-top:22px}
.foot-contact .bar{width:1px;height:20px;background:rgba(255,255,255,.6)}
.socials{display:flex;gap:14px;margin-top:28px}
.socials span{width:22px;height:22px;border-radius:50%;background:var(--white)}
.quick-links{width:230px}
.quick-links a{display:block;color:var(--white);text-decoration:none;font-size:12px;height:40px;line-height:40px;border-bottom:1px solid rgba(255,255,255,.7)}
.quick-links a:last-child{border-bottom:none}
.quick-links h5{margin-bottom:6px}
.newsletter p{font-size:11px;line-height:20px;margin-top:18px;width:200px}
.newsletter .field{width:262px;height:34px;background:var(--white);margin-top:10px;color:#555;font-size:11px;padding-left:9px;line-height:34px}
.newsletter .subscribe{width:136px;height:32px;border-radius:16px;background:var(--red);margin-top:15px;text-align:center;line-height:32px;font-size:13px}
.copyright{top:3152px;height:60px;background:var(--black);color:var(--white);font-size:12px;line-height:60px;padding-left:92px}
</style>
</head>
<body>

<div class="section top-bar">
  <div class="contact">
    <span><svg width="12" height="12" viewBox="0 0 24 24" fill="#fff"><path d="M6.6 10.8a15 15 0 006.6 6.6l2.2-2.2c.3-.3.7-.4 1-.2 1.1.4 2.3.6 3.6.6.6 0 1 .4 1 1V20c0 .6-.4 1-1 1A17 17 0 013 4c0-.6.4-1 1-1h3.5c.6 0 1 .4 1 1 0 1.3.2 2.5.6 3.6.1.3 0 .7-.2 1z"/></svg>352-555-0148</span>
    <span class="divider"></span>
    <span><svg width="12" height="10" viewBox="0 0 24 18" fill="#fff"><path d="M0 0h24v18H0z" opacity=".9"/><path d="M0 0l12 9 12-9" stroke="#f04a50" stroke-width="2" fill="none"/></svg>hello@gwenshines.net</span>
  </div>
  <div class="estimate">REQUEST A FREE ESTIMATE</div>
</div>

<header class="section site-header">
  <div class="brand"><span class="mark"></span>GWEN SHINES</div>
  <nav class="main-nav">
    <a class="active" href="#">HOME</a><a href="#">ABOUT US</a><a href="#">SERVICES</a><a href="#">WHAT WE PROVIDE</a><a href="#">CONTACT US</a>
  </nav>
</header>

<section class="section hero">
  <div class="hero-photo" role="img" aria-label="Woman in a red shirt and yellow gloves wiping a kitchen oven"></div>
  <div class="hero-box">
    <h1>RELIABLE &amp; HONEST</h1>
    <p>Our mission at Gwen's Cleaning is simple: to provide high-quality services for our valued clients</p>
    <ul class="hero-list">
      <li><svg width="20" height="20" viewBox="0 0 20 20" fill="none" stroke="#fff" stroke-width="2"><circle cx="10" cy="10" r="8"/><path d="M6 10l3 3 8-9"/></svg>Bedroom Interior</li>
      <li><svg width="20" height="20" viewBox="0 0 20 20" fill="none" stroke="#fff" stroke-width="2"><circle cx="10" cy="10" r="8"/><path d="M6 10l3 3 8-9"/></svg>Dining Room</li>
      <li><svg width="20" height="20" viewBox="0 0 20 20" fill="none" stroke="#fff" stroke-width="2"><circle cx="10" cy="10" r="8"/><path d="M6 10l3 3 8-9"/></svg>Bathrooms</li>
      <li><svg width="20" height="20" viewBox="0 0 20 20" fill="none" stroke="#fff" stroke-width="2"><circle cx="10" cy="10" r="8"/><path d="M6 10l3 3 8-9"/></svg>Living Room</li>
      <li><svg width="20" height="20" viewBox="0 0 20 20" fill="none" stroke="#fff" stroke-width="2"><circle cx="10" cy="10" r="8"/><path d="M6 10l3 3 8-9"/></svg>Kitchen</li>
      <li><svg width="20" height="20" viewBox="0 0 20 20" fill="none" stroke="#fff" stroke-width="2"><circle cx="10" cy="10" r="8"/><path d="M6 10l3 3 8-9"/></svg>Kids Rooms</li>
    </ul>
    <span class="btn-outline">SCHEDULE FREE ONLINE ESTIMATE</span>
  </div>
</section>

<section class="section provide" role="group">
  <div class="provide-text">
    <h2>WHAT WE PROVIDE</h2>
    <h3>WEEKLY, BI-WEEKLY, MONTHLY OR CUSTOM CLEANS AVAILABLE</h3>
    <p>Attention to Detail<br>Since its founding, Gwen Shines has been one of the most trusted names in the industry. Hire us for this service and learn how we cater to the needs of each client, ensuring the results you need and deserve.</p>
    <span class="btn-outline">ABOUT US</span>
  </div>
  <div class="provide-photo" role="img" aria-label="Red flat mop on a wooden floor"></div>
</section>

<section class="section services">
  <h2>MOVE IN &amp; OUT CLEANING</h2>
  <div class="sub">EXPERT SERVICE</div>
  <p class="lead">We have the experience and skills necessary to tackle just about every type of job that comes our way. With Gwen Shines, clients know exactly what to expect - professionalism, efficiency and exceptional results.</p>

  <div class="service-card" style="left:158px">
    <div class="ring"><svg width="100" height="90" viewBox="0 0 100 90" fill="none" stroke="#f04a50" stroke-width="4"><rect x="12" y="10" width="76" height="34" rx="3"/><rect x="24" y="26" width="22" height="14" rx="4"/><rect x="54" y="26" width="22" height="14" rx="4"/><rect x="6" y="44" width="88" height="26" rx="3"/><path d="M6 58h88M14 70v12M86 70v12"/></svg></div>
    <h4>BEDROOM</h4>
  </div>
  <div class="service-card" style="left:459px">
    <div class="ring"><svg width="110" height="100" viewBox="0 0 110 100" fill="none" stroke="#f04a50" stroke-width="4"><path d="M10 52h90v12a20 20 0 01-20 20H30a20 20 0 01-20-20z"/><path d="M28 84l-4 10M82 84l4 10M80 52V16a8 8 0 00-16 0v4"/><path d="M58 22h14"/><circle cx="22" cy="46" r="5"/><circle cx="34" cy="42" r="5"/><path d="M60 32v4M66 32v4M72 32v4M60 42v4M66 42v4M72 42v4"/></svg></div>
    <h4>BATHROOM</h4>
  </div>
  <div class="service-card" style="left:758px">
    <div class="ring"><svg width="100" height="100" viewBox="0 0 100 100" fill="none" stroke="#f04a50" stroke-width="4"><path d="M10 30l8-16h14l8 16zM25 14V4"/><path d="M52 6v26M48 32h8"/><rect x="8" y="52" width="44" height="40"/><path d="M8 64h44M30 64v28M18 58h4M36 58h4"/><rect x="62" y="34" width="30" height="58"/><path d="M62 56h30M68 44v6M68 64v10"/></svg></div>
    <h4>KITCHEN</h4>
  </div>

  <span class="btn-outline">VIEW ALL SERVICES</span>
</section>

<section class="section hours">
  <div class="hours-card">
    <div class="inner">
      <h2>OPENING HOURS</h2>
      <div class="note">CONTACT BY TEXT AFTER 9AM -10PM</div>
      <div class="label">AVAILABLE CLEANING TIME</div>
      <div class="time">MON - FRI:&nbsp; 9AM - 5PM</div>
      <div class="time">SATURDAY- SUNDAY:&nbsp;&nbsp; 9AM - 5PM</div>
    </div>
  </div>
  <div class="contact-tile" style="top:96px;height:97px">
    <div class="inner"><svg width="50" height="50" viewBox="0 0 50 50" fill="none" stroke="#f04a50" stroke-width="2"><path d="M12 6l8 10-5 5c3 6 8 11 14 14l5-5 10 8-5 7C24 44 6 26 5 11z"/><path d="M30 8a14 14 0 0112 12M30 14a8 8 0 016 6"/></svg>352-555-0148</div>
  </div>
  <div class="contact-tile" style="top:245px;height:100px">
    <div class="inner"><svg width="56" height="40" viewBox="0 0 56 40" fill="none" stroke="#f04a50" stroke-width="2"><rect x="2" y="2" width="52" height="36"/><path d="M2 2l26 20 26-20M2 38l19-18M54 38L35 20"/></svg>hello@gwenshines.net</div>
  </div>
</section>

<section class="section news">
  <h2>TIPS, NEWS, &amp; UPDATES</h2>
  <article class="post" style="left:100px">
    <div class="thumb" role="img" aria-label="Woman mopping a bright kitchen floor" style="background:linear-gradient(135deg,#f1f1f1,#d9dcdf 60%,#9fc9e0)"></div>
    <h3>HEADING TITLE HERE</h3>
    <p>Lorem Ipsum is simply dummy text of the printing and typesetting industry. Lorem Ipsum has been dummy text ever since the 1500s.</p>
    <div class="more">READ MORE <svg width="5" height="7" viewBox="0 0 5 7" fill="#f04a50"><path d="M0 0l5 3.5L0 7z"/></svg></div>
  </article>
  <article class="post" style="left:461px">
    <div class="thumb" role="img" aria-label="Gloved hand cleaning a bathroom sink with spray" style="background:linear-gradient(135deg,#cfe8f2,#e9a25a 55%,#f3f3f3)"></div>
    <h3>HEADING TITLE HERE</h3>
    <p>Lorem Ipsum is simply dummy text of the printing and typesetting industry. Lorem Ipsum has been dummy text ever since the 1500s.</p>
    <div class="more">READ MORE <svg width="5" height="7" viewBox="0 0 5 7" fill="#f04a50"><path d="M0 0l5 3.5L0 7z"/></svg></div>
  </article>
  <article class="post" style="left:822px">
    <div class="thumb" role="img" aria-label="Bucket of cleaning supplies in a living room" style="background:linear-gradient(135deg,#6b6663,#b5aca4 50%,#d6453e 75%,#8a7a6c)"></div>
    <h3>HEADING TITLE HERE</h3>
    <p>Lorem Ipsum is simply dummy text of the printing and typesetting industry. Lorem Ipsum has been dummy text ever since the 1500s.</p>
    <div class="more">READ MORE <svg width="5" height="7" viewBox="0 0 5 7" fill="#f04a50"><path d="M0 0l5 3.5L0 7z"/></svg></div>
  </article>
</section>

<footer class="section site-footer">
  <div class="foot-col foot-contact" style="left:91px">
    <h5>CONTACT US</h5>
    <div><svg width="13" height="13" viewBox="0 0 24 24" fill="#fff"><path d="M6.6 10.8a15 15 0 006.6 6.6l2.2-2.2c.3-.3.7-.4 1-.2 1.1.4 2.3.6 3.6.6.6 0 1 .4 1 1V20c0 .6-.4 1-1 1A17 17 0 013 4c0-.6.4-1 1-1h3.5c.6 0 1 .4 1 1 0 1.3.2 2.5.6 3.6.1.3 0 .7-.2 1z"/></svg><span class="bar"></span>352-555-0148</div>
    <div><svg width="14" height="10" viewBox="0 0 24 18" fill="#fff"><path d="M0 0h24v18H0z"/><path d="M0 0l12 9 12-9" stroke="#3189b1" stroke-width="2" fill="none"/></svg><span class="bar"></span>hello@gwenshines.net</div>
    <div class="socials" aria-label="Social links"><span></span><span></span><span></span><span></span></div>
  </div>
  <div class="foot-col quick-links" style="left:488px">
    <h5>QUICK LINKS</h5>
    <a href="#">ABOUT US</a><a href="#">SERVICES</a><a href="#">WHAT WE PROVIDE</a><a href="#">TERMS &amp; CONDITION</a><a href="#">CONTACT US</a>
  </div>
  <div class="foot-col newsletter" style="left:833px">
    <h5>NEWSLETTER</h5>
    <p>SIGN UP FOR THE LATEST NEWS, OFFERS AND STYLES</p>
    <div class="field">Your Email</div>
    <div class="subscribe">SUBSCRIBE</div>
  </div>
</footer>

<div class="section copyright">© 2019 GWEN SHINES&nbsp; ALL RIGHTS RESERVED</div>

</body>
</html>
```